依頼詳細
パッケージは、台紙にブリスターケース。
台紙サイズ縦155mm×横90mm
容器は、左下に設置します。
容器サイズは、93mm×横19mm
ブランド名、MIRETO 商品名、TOMARU for Menは必ず入れてください。
キャッチコピー…出来る男の花粉対策という文字を入れてください。
記載項目
写真はフォトリンデルの№38261507の男性を使ってください
※すでに契約しています
希望イメージ
シンプル 複雑
単色 カラフル
暗い 明るい
日常 高級
遊び心 厳粛
未来的 伝統的
女性的 男性的
希望する色
納品ファイル
• 高解像度JPG (.jpg)
• イラストレーター形式 (.ai)
補足説明
販売価格が1500円前後。買いやすい設定にしています。男性が気軽に手に取れるパッケージをお願いします。
写真は、添付したものをご使用ください。(契約済み)

```html
<!DOCTYPE html>
<html lang="ja">
<head>
<meta charset="utf-8">
<title>MIRETO TOMARU for MEN — Blister Card</title>
<link rel="stylesheet" href="https://fonts.googleapis.com/css2?family=Bodoni+Moda:wght@400;500&family=Noto+Serif+JP:wght@500&display=swap">
<style>
  :root {
    --card-black: #0c0c0c;
    --ink-white: #ffffff;
    --dash-grey: #8a8a8a;
    --photo-dark: #1b2430;
    --photo-mid: #4a4a4e;
    --photo-light: #8c8a88;
  }
  * { margin: 0; padding: 0; box-sizing: border-box; }
  html, body {
    width: 698px;
    height: 1200px;
    overflow: hidden;
    background: #ffffff;
  }
  .card {
    position: relative;
    width: 698px;
    height: 1200px;
    background: var(--card-black);
    border-radius: 14px;
    overflow: hidden;
    color: var(--ink-white);
  }
  .hang-hole {
    position: absolute;
    left: 274px;
    top: 68px;
    width: 150px;
    height: 28px;
    border-radius: 14px;
    background: #ffffff;
  }
  .brand {
    position: absolute;
    right: 47px;
    top: 24px;
    font-family: "Bodoni Moda", serif;
    font-weight: 500;
    font-size: 28px;
    letter-spacing: 1px;
  }
  .photo-frame {
    position: absolute;
    left: 174px;
    top: 140px;
    width: 477px;
    height: 604px;
    background: var(--ink-white);
    padding: 8px;
  }
  .photo-frame .photo {
    width: 100%;
    height: 100%;
    background:
      radial-gradient(ellipse at 55% 30%, var(--photo-light) 0%, transparent 45%),
      linear-gradient(160deg, var(--photo-dark) 0%, var(--photo-mid) 55%, #1e1e20 100%);
  }
  .blister-slot {
    position: absolute;
    left: 70px;
    top: 419px;
    width: 144px;
    height: 651px;
    border: 2px dashed var(--dash-grey);
  }
  .product-name {
    font-family: "Bodoni Moda", serif;
    font-weight: 400;
  }
  .product-name .line {
    position: absolute;
    left: 250px;
    font-size: 200px;
    line-height: 0.72;
    letter-spacing: -4px;
    white-space: nowrap;
    transform: scaleX(0.74);
    transform-origin: left top;
  }
  .product-name .line-1 { top: 756px; }
  .product-name .line-2 { top: 905px; }
  .product-name .for-men {
    position: absolute;
    left: 470px;
    top: 993px;
    font-size: 40px;
    line-height: 1;
    white-space: nowrap;
  }
  .catch-copy {
    position: absolute;
    left: 252px;
    top: 1056px;
    font-family: "Noto Serif JP", serif;
    font-weight: 500;
    font-size: 30px;
    line-height: 1.2;
    letter-spacing: 14px;
    white-space: nowrap;
  }
  .catch-rule {
    position: absolute;
    left: 250px;
    top: 1104px;
    width: 405px;
    height: 2px;
    background: var(--ink-white);
  }
</style>
</head>
<body>
  <div class="card">
    <div class="hang-hole"></div>
    <div class="brand">MIRETO</div>

    <div class="photo-frame">
      <div class="photo" role="img" aria-label="Photograph of a man in a knit scarf holding a tissue to his nose"></div>
    </div>

    <div class="blister-slot"></div>

    <h1 class="product-name">
      <span class="line line-1">TOMA</span>
      <span class="line line-2">RU</span>
      <span class="for-men">for MEN</span>
    </h1>

    <p class="catch-copy">デキる男の花粉対策</p>
    <div class="catch-rule"></div>
  </div>
</body>
</html>
```